Velter Labs - Mushroom Supplement Packaging

Our brand is called Velter Labs. I've added a couple different logos that you can use. We are creating a line up of Mushroom Supplement products. I will add the entire line-up of products here. I've added examples of other products and packaging shape types I can purchase. Give me different options for packaging that is minimalist and clean for this brand that makes it look really well made and clean and make people want to buy.

Product 1 Lions Mane 1g
Product 2 Cordyceps 1g
Product 3 Chaga 1g
Product 4 Turkey Tail 1g
Product 5 Reishi 1g
Product 6 Maitake 1g
Product 7 Shiitake 1g

Product 8 (Mix) Lions Mane 143mg
Cordyceps 143mg
Chaga 143mg
Turkey Tail 143mg
Reishi 143mg
Maitake 143mg
Shiitake 143mg

```html
<!DOCTYPE html>
<html lang="en">
<head>
<meta charset="utf-8">
<title>Velter Labs – Mushroom Supplement Packaging</title>
<link rel="stylesheet" href="https://fonts.googleapis.com/css2?family=Montserrat:wght@300;400;500;600;700&display=swap">
<style>
  :root{
    --bg:#5a5b5e;
    --jar:#141414;
    --jar-hi:#2c2c2c;
    --gold:#b08736;
    --gold-deep:#6f4a1c;
    --gold-light:#d9b26a;
    --ink:#262220;
    --maitake:#5f8a64;
    --mix:#8e7ba2;
    --chaga:#7c87ab;
    --cordyceps:#c98d4f;
    --lionsmane:#5a94aa;
    --shiitake:#c9a95d;
    --reishi:#c9705c;
    --turkeytail:#d2667e;
  }
  *{box-sizing:border-box;margin:0;padding:0}
  html,body{width:1200px;height:900px;overflow:hidden}
  body{background:var(--bg);font-family:"Montserrat",sans-serif;position:relative}

  .jar{position:absolute;width:calc(var(--u)*16.4);display:flex;flex-direction:column;--name:var(--gold)}
  .jar--small{--u:10px;top:124px}
  .jar--large{--u:16.6px;top:443px}
  .jar--hero{--u:19.1px;top:429px}
  .jar--deep-name{--name:var(--gold-deep)}

  .jar__lid{height:calc(var(--u)*3.9);border-radius:calc(var(--u)*0.7) calc(var(--u)*0.7) calc(var(--u)*0.3) calc(var(--u)*0.3);
    background:linear-gradient(180deg,var(--jar-hi),var(--jar) 60%)}
  .jar__neck{height:calc(var(--u)*0.6);margin:0 calc(var(--u)*0.4);background:var(--jar)}
  .jar__label{height:calc(var(--u)*11);display:flex;flex-direction:column;align-items:center;text-align:center;
    padding-top:calc(var(--u)*1.2);
    background:linear-gradient(90deg,var(--tone),color-mix(in srgb,var(--tone) 80%,#000) 100%)}
  .jar__base{height:calc(var(--u)*3.3);border-radius:calc(var(--u)*0.2) calc(var(--u)*0.2) calc(var(--u)*1) calc(var(--u)*1);
    background:var(--jar);display:flex;justify-content:center;padding-top:calc(var(--u)*0.6);color:var(--gold-light)}

  .brand{font-weight:600;font-size:calc(var(--u)*1.35);letter-spacing:0.06em;color:var(--ink);
    text-transform:uppercase;line-height:1}
  .product{font-weight:300;font-size:calc(var(--u)*2.3);line-height:1;color:var(--name);margin-top:calc(var(--u)*1.1)}
  .product--long{font-size:calc(var(--u)*1.45);margin-top:calc(var(--u)*1.5);margin-bottom:calc(var(--u)*0.4)}
  .line{font-size:calc(var(--u)*0.62);letter-spacing:0.12em;color:var(--ink);text-transform:uppercase;line-height:1;
    margin-top:calc(var(--u)*0.5)}
  .divider{width:calc(var(--u)*11);height:1px;background:var(--name);margin-top:calc(var(--u)*0.7)}
  .tagline{font-size:calc(var(--u)*0.58);font-weight:700;letter-spacing:0.12em;color:var(--ink);text-transform:uppercase;
    line-height:1;margin-top:calc(var(--u)*0.8)}
  .sub{font-size:calc(var(--u)*0.6);letter-spacing:0.06em;color:var(--ink);line-height:1.3;margin-top:calc(var(--u)*0.25)}
  .sub--list{margin-top:calc(var(--u)*0.8)}
  .facts{font-size:calc(var(--u)*0.56);letter-spacing:0.1em;text-transform:uppercase;line-height:1}
  .facts b{font-weight:700}
  .facts span{margin:0 0.8em}
</style>
</head>
<body>

<div class="jar jar--small" style="left:151px;--tone:var(--maitake)">
  <div class="jar__lid"></div><div class="jar__neck"></div>
  <div class="jar__label">
    <div class="brand">Velter Labs</div>
    <div class="product">maitake</div>
    <div class="line">Mushroom Brain Booster</div>
    <div class="divider"></div>
    <div class="tagline">Immunity Mushroom</div>
    <div class="sub">Support Your Health Heart</div>
  </div>
  <div class="jar__base"><p class="facts"><b>60 Capsules</b><span>•</span>Dietary Supplement</p></div>
</div>

<div class="jar jar--small" style="left:335px;--tone:var(--mix)">
  <div class="jar__lid"></div><div class="jar__neck"></div>
  <div class="jar__label">
    <div class="brand">Velter Labs</div>
    <div class="product product--long">(mix) lion's mane</div>
    <div class="line">Mushroom Brain Booster</div>
    <div class="divider"></div>
    <div class="sub sub--list">Cordyceps, Chaga, Turkey Tail<br>Reishi, Maitake, Shiitake</div>
  </div>
  <div class="jar__base"><p class="facts"><b>60 Capsules</b><span>•</span>Dietary Supplement</p></div>
</div>

<div class="jar jar--small" style="left:519px;--tone:var(--chaga)">
  <div class="jar__lid"></div><div class="jar__neck"></div>
  <div class="jar__label">
    <div class="brand">Velter Labs</div>
    <div class="product">chaga</div>
    <div class="line">Mushroom Brain Booster</div>
    <div class="divider"></div>
    <div class="tagline">Vitality Mushroom</div>
    <div class="sub">Rejuvenate Your Body</div>
  </div>
  <div class="jar__base"><p class="facts"><b>60 Capsules</b><span>•</span>Dietary Supplement</p></div>
</div>

<div class="jar jar--small jar--deep-name" style="left:703px;--tone:var(--cordyceps)">
  <div class="jar__lid"></div><div class="jar__neck"></div>
  <div class="jar__label">
    <div class="brand">Velter Labs</div>
    <div class="product">cordyceps</div>
    <div class="line">Mushroom Brain Booster</div>
    <div class="divider"></div>
    <div class="tagline">Endurance Mushroom</div>
    <div class="sub">Boost Your Energy</div>
  </div>
  <div class="jar__base"><p class="facts"><b>60 Capsules</b><span>•</span>Dietary Supplement</p></div>
</div>

<div class="jar jar--small" style="left:886px;--tone:var(--lionsmane)">
  <div class="jar__lid"></div><div class="jar__neck"></div>
  <div class="jar__label">
    <div class="brand">Velter Labs</div>
    <div class="product">lion's mane</div>
    <div class="line">Mushroom Brain Booster</div>
    <div class="divider"></div>
    <div class="tagline">Smart Mushroom</div>
    <div class="sub">Improve Your Focus</div>
  </div>
  <div class="jar__base"><p class="facts"><b>60 Capsules</b><span>•</span>Dietary Supplement</p></div>
</div>

<div class="jar jar--large jar--deep-name" style="left:137px;--tone:var(--shiitake)">
  <div class="jar__lid"></div><div class="jar__neck"></div>
  <div class="jar__label">
    <div class="brand">Velter Labs</div>
    <div class="product">shiitake</div>
    <div class="line">Mushroom Brain Booster</div>
    <div class="divider"></div>
    <div class="tagline">Energize Mushroom</div>
    <div class="sub">Immune and Cellular Support</div>
  </div>
  <div class="jar__base"><p class="facts"><b>60 Capsules</b><span>•</span>Dietary Supplement</p></div>
</div>

<div class="jar jar--hero" style="left:443px;--tone:var(--reishi)">
  <div class="jar__lid"></div><div class="jar__neck"></div>
  <div class="jar__label">
    <div class="brand">Velter Labs</div>
    <div class="product">reishi</div>
    <div class="line">Mushroom Brain Booster</div>
    <div class="divider"></div>
    <div class="tagline">Immortality Mushroom</div>
    <div class="sub">Vitality, Healthy Aging &amp; Longevity</div>
  </div>
  <div class="jar__base"><p class="facts"><b>60 Capsules</b><span>•</span>Dietary Supplement</p></div>
</div>

<div class="jar jar--large" style="left:792px;--tone:var(--turkeytail)">
  <div class="jar__lid"></div><div class="jar__neck"></div>
  <div class="jar__label">
    <div class="brand">Velter Labs</div>
    <div class="product">turkey tail</div>
    <div class="line">Mushroom Brain Booster</div>
    <div class="divider"></div>
    <div class="tagline">Immunity Mushroom</div>
    <div class="sub">Supercharge Your Health</div>
  </div>
  <div class="jar__base"><p class="facts"><b>60 Capsules</b><span>•</span>Dietary Supplement</p></div>
</div>

</body>
</html>
```